Art and Artifact Selling classy website.

I am into selling of Art works and artifacts. The art work range from different type such as animation, architecture, assemblage, calligraphy, computer, Christian or religious, conceptual, artistic design, drawing, folk, graffiti, graphic, illuminated manuscript, illustration, mosaic, painting, performance, photography, sculpture. This website will feature categories of the above art works. My website should have images of the above art works and should be classy. My business is based in the United States and my target customers are Americans. Different artistic colors are welcome. My business name is quenmarsh Art.

Industry/Entity Type

Architecture

Coding

Coded - Design and coding required

```html
<!DOCTYPE html>
<html lang="en">
<head>
<meta charset="utf-8">
<title>quenmarsh Art</title>
<link href="https://fonts.googleapis.com/css2?family=Lato:ital,wght@0,400;0,700;1,400;1,700&family=Roboto:wght@400;500&display=swap" rel="stylesheet">
<style>
:root{
  --teal:#0aa38b;
  --purple:#8e3a93;
  --sky:#4ec2da;
  --blue:#0c8dd0;
  --lime:#9cc63a;
  --jade:#05a68c;
  --plum:#a1449b;
  --ink:#333333;
  --muted:#777777;
  --nav:#555555;
  --header:#f7f6f8;
  --grey-band:#e6e6e7;
  --soft:#f5f3f4;
  --navy:#363c58;
  --white:#ffffff;
}
*{margin:0;padding:0;box-sizing:border-box}
html,body{width:1200px;height:2406px;overflow:hidden}
body{position:relative;background:var(--white);font-family:"Lato",sans-serif;color:var(--ink)}
.abs{position:absolute}

/* header */
.site-header{left:0;top:0;width:1200px;height:125px;background:var(--header)}
.brand{left:75px;top:34px;font-family:"Lato",sans-serif;font-weight:700;font-size:50px;color:var(--teal);letter-spacing:-0.5px}
.login{left:1040px;top:22px;width:84px;height:33px;border-radius:17px;background:var(--sky);color:var(--white);font:500 12px/33px "Roboto",sans-serif;text-align:center}
.main-nav{right:76px;top:69px;display:flex;gap:8px;list-style:none}
.main-nav li{font:400 13px/32px "Roboto",sans-serif;color:var(--nav);padding:0 16px}
.main-nav li.active{border:2px solid var(--purple);border-radius:17px;color:var(--purple);line-height:28px;padding:0 20px}

/* hero */
.hero{left:0;top:125px;width:1200px;height:510px;background:
  linear-gradient(180deg,rgba(0,0,0,.12),rgba(0,0,0,.25)),
  linear-gradient(170deg,#7c7a2b 0%,#a09a30 22%,#5d5a2a 38%,#5b3320 52%,#2f6a7a 68%,#5b8c92 82%,#7a5440 100%)}
.hero-title{left:0;width:1200px;top:138px;text-align:center;font:italic 700 55px "Lato",sans-serif;color:var(--white)}
.hero-text{left:250px;width:700px;top:226px;text-align:center;font:400 15.5px/23px "Lato",sans-serif;color:var(--white)}
.hero-btn{left:518px;top:305px;width:165px;height:44px;border:2px solid var(--white);border-radius:22px;color:var(--white);font:500 12px/40px "Roboto",sans-serif;text-align:center}
.hero-dots{left:1125px;top:224px}
.hero-dots span{display:block;width:13px;height:13px;border-radius:50%;border:2px solid var(--white);margin-bottom:16px}
.hero-dots span.on{background:var(--white)}

/* section headings */
.section-title{left:0;width:1200px;text-align:center;font:500 25px "Roboto",sans-serif;color:var(--ink)}
.rule{width:37px;height:3px;background:var(--teal);left:582px}

.range-intro{left:90px;width:1020px;top:765px;text-align:center;font:italic 400 15px/22px "Lato",sans-serif;color:var(--muted)}
.grey-band{left:0;top:982px;width:1200px;height:240px;background:linear-gradient(180deg,#e2e2e3,#f3f3f3)}
.categories{left:0;top:840px}
.cat{position:absolute;width:263px;text-align:center;color:var(--white)}
.cat h3{font:italic 400 22px "Lato",sans-serif;margin-top:10px}
.cat p{font:400 13px/17px "Lato",sans-serif;margin-top:14px}
.carousel-nav{left:550px;top:1147px;width:100px;height:40px}

/* welcome */
.welcome-lead{left:0;width:1200px;top:1369px;text-align:center;font:italic 400 16px "Lato",sans-serif;color:var(--teal)}
.welcome-text{left:95px;width:1010px;top:1400px;text-align:center;font:400 13.5px/22px "Lato",sans-serif;color:var(--muted)}
.btn-teal{background:var(--teal);color:var(--white);border-radius:19px;font:500 12px/37px "Roboto",sans-serif;text-align:center}
.welcome-btn{left:536px;top:1487px;width:131px;height:37px}

/* featured video */
.featured{left:0;top:1596px;width:1200px;height:411px;background:var(--soft)}
.featured-title{left:74px;top:1664px;font:500 23px "Roboto",sans-serif;color:var(--ink)}
.featured-text{left:74px;width:490px;font:400 13px/22px "Lato",sans-serif;color:var(--muted)}
.featured-btn{left:75px;top:1894px;width:187px;height:37px}
.featured-media{left:582px;top:1596px}

/* newsletter */
.newsletter{left:74px;top:2068px;width:1054px;height:125px;background:var(--teal)}
.newsletter h2{position:absolute;left:208px;top:24px;font:500 23px "Roboto",sans-serif;color:var(--white)}
.newsletter p{position:absolute;left:208px;top:60px;font:italic 400 15px/21px "Lato",sans-serif;color:var(--white)}
.signup-field{position:absolute;left:505px;top:44px;width:505px;height:41px;border-radius:21px;background:var(--white)}
.signup-field span{position:absolute;left:30px;top:0;font:italic 400 12px/41px "Lato",sans-serif;color:#999}
.signup-btn{position:absolute;right:0;top:0;width:127px;height:41px;border-radius:21px;background:var(--navy);color:var(--white);font:500 13px/41px "Roboto",sans-serif;text-align:center}

/* footer */
.site-footer{left:0;top:2246px;width:1200px;height:160px;background:var(--navy);color:var(--white)}
.footer-title{left:75px;top:36px;font:italic 400 21px "Lato",sans-serif}
.footer-line{font:400 12.5px/21px "Lato",sans-serif}
.social{top:50px;width:34px;height:34px;border-radius:50%}
.copyright{right:76px;top:97px;font:400 12.5px "Lato",sans-serif}
</style>
</head>
<body>

<header class="abs site-header">
  <div class="abs brand">quenmarsh Art</div>
  <div class="abs login">LOGIN</div>
  <ul class="abs main-nav">
    <li class="active">HOME</li>
    <li>ABOUT US</li>
    <li>EVENTS</li>
    <li>RESOURCES</li>
    <li>ARTICLES</li>
    <li>CONTACT US</li>
  </ul>
</header>

<section class="abs hero" role="img" aria-label="Close-up of thick textured oil paint strokes in olive, rust and teal">
  <h1 class="abs hero-title">Art Works &amp; Artifacts</h1>
  <p class="abs hero-text">Nam dignissim id lorem at interdum. Nam vel molestie sem, vitae imperdiet ipsum. Curabitur tincidunt aliquet egestas. Vivamus maximus sodales</p>
  <div class="abs hero-btn">LEARN MORE</div>
  <div class="abs hero-dots"><span class="on"></span><span></span><span></span></div>
</section>

<h2 class="abs section-title" style="top:705px">ART WORK RANGE FROM DIFFERENT TYPE</h2>
<div class="abs rule" style="top:741px"></div>
<p class="abs range-intro">The art work range from different type such as animation, architecture, assemblage, calligraphy, computer, Christian or religious, conceptual, artistic design, drawing, folk, graffiti, graphic, illuminated manuscript, illustration, mosaic, painting, performance, photography, sculpture.</p>

<div class="abs grey-band"></div>
<svg class="abs" style="left:0;top:0" width="1200" height="1120" viewBox="0 0 1200 1120" aria-hidden="true">
  <polygon points="74,845 337,873 337,1076 74,1104" fill="var(--blue)"/>
  <polygon points="337,873 602,843 602,1103 337,1076" fill="var(--lime)"/>
  <polygon points="602,843 865,871 865,1076 602,1103" fill="var(--jade)"/>
  <polygon points="865,871 1128,842 1128,1102 865,1076" fill="var(--plum)"/>
  <g fill="none" stroke="#fff" stroke-width="3" stroke-linejoin="round" stroke-linecap="round">
    <!-- cube -->
    <polygon points="203,895 231,910 231,942 203,957 175,942 175,910"/>
    <polyline points="175,910 203,925 231,910"/><line x1="203" y1="925" x2="203" y2="957"/>
    <!-- ruler & pencil -->
    <line x1="445" y1="900" x2="491" y2="946" stroke-width="9"/>
    <line x1="491" y1="900" x2="445" y2="946" stroke-width="7"/>
    <!-- pen -->
    <line x1="745" y1="898" x2="712" y2="938" stroke-width="8"/>
    <line x1="702" y1="953" x2="752" y2="953"/>
    <!-- laptop -->
    <rect x="972" y="900" width="50" height="34" rx="2"/>
    <polyline points="962,944 1032,944 1028,952 966,952"/>
  </g>
</svg>
<div class="abs categories">
  <div class="cat" style="left:74px;top:130px"><h3>Animation</h3><p>Curabitur vitae malesuada tellus,<br>Nunc congue od.</p></div>
  <div class="cat" style="left:337px;top:130px"><h3>Architecture</h3><p>Curabitur vitae malesuada tellus,<br>Nunc congue od.</p></div>
  <div class="cat" style="left:602px;top:130px"><h3>Calligraphy</h3><p>Curabitur vitae malesuada tellus,<br>Nunc congue od.</p></div>
  <div class="cat" style="left:865px;top:130px"><h3>Computer</h3><p>Curabitur vitae malesuada tellus,<br>Nunc congue od.</p></div>
</div>
<svg class="abs carousel-nav" viewBox="0 0 100 40" aria-hidden="true">
  <circle cx="19" cy="20" r="17" fill="none" stroke="#999" stroke-width="1.5"/>
  <polyline points="22,14 16,20 22,26" fill="none" stroke="#999" stroke-width="1.5"/>
  <line x1="50" y1="0" x2="50" y2="40" stroke="#ccc"/>
  <circle cx="82" cy="20" r="17" fill="none" stroke="#ccc" stroke-width="1.5"/>
  <polyline points="79,14 85,20 79,26" fill="none" stroke="#ccc" stroke-width="1.5"/>
</svg>

<h2 class="abs section-title" style="top:1300px">WELCOME TO QUENMARSH ART</h2>
<div class="abs rule" style="top:1334px"></div>
<p class="abs welcome-lead">I am into selling of Art works and artifacts.</p>
<p class="abs welcome-text">Aliquam non dui sapien. Curabitur sed efficitur dui. Suspendisse sed egestas purus, posuere vehicula tellus. Nullam efficitur nulla id porta tincidunt. Nulla consequat cursus faucibus. Mauris a tellus sagittis, commodo eros at, sodales libero. Aenean laoreet, arcu in hendrerit pharetra, enim nisl consectetur nibh, ac feugiat quam Aliquam non dui sapien. Curabitur sed efficitur dui. Suspendisse sed egestas purus, posuere vehicula tellus.</p>
<div class="abs btn-teal welcome-btn">READ MORE</div>

<section class="abs featured"></section>
<h2 class="abs featured-title">FEATURED VIDEO</h2>
<p class="abs featured-text" style="top:1713px">Nunc eget nibh sed eros dictum tincidunt in commodo nunc. Integer tincidunt rhoncus eros non hendrerit. Nam dignissim id lorem at interdum. Nam vel molestie sem, vitae imperdiet ipsum. Curabitur tincidunt</p>
<p class="abs featured-text" style="top:1802px">Aliquet egestas. Vivamus maximus sodales ligula et feugiat. Mauris vitae tincidunt purus. Fusce consequat justo vel diam rhoncus, vel eleifend risus pellentesque. Suspendisse potenti.</p>
<div class="abs btn-teal featured-btn">WATCH MORE VIDEOS</div>
<svg class="abs featured-media" width="618" height="411" viewBox="0 0 618 411" role="img" aria-label="Video still of an ancient plaster figure among stone pots and urns in a dim museum storeroom">
  <defs>
    <linearGradient id="mediaTone" x1="0" y1="0" x2="1" y2="1">
      <stop offset="0" stop-color="#4a4744"/>
      <stop offset="0.5" stop-color="#7a766f"/>
      <stop offset="1" stop-color="#3a3835"/>
    </linearGradient>
  </defs>
  <polygon points="72,0 618,0 618,411 0,411" fill="url(#mediaTone)"/>
  <circle cx="323" cy="205" r="44" fill="none" stroke="#fff" stroke-width="4"/>
  <polygon points="311,184 342,205 311,226" fill="none" stroke="#fff" stroke-width="4" stroke-linejoin="round"/>
</svg>

<section class="abs newsletter">
  <h2>NEWSLETTER</h2>
  <p>Signup for our newsletter and update<br>your self regulary</p>
  <div class="signup-field"><span>Email Address</span><div class="signup-btn">SIGNUP</div></div>
</section>

<footer class="abs site-footer">
  <h2 class="abs footer-title">Contact Info</h2>
  <div class="abs footer-line" style="left:75px;top:77px">ADDRESS</div>
  <div class="abs footer-line" style="left:154px;top:77px">418 LARKFIELD AVE.<br>BRENMOOR, MA 02187</div>
  <svg class="abs" style="left:364px;top:80px" width="14" height="40" viewBox="0 0 14 40" aria-hidden="true">
    <path d="M2 2 L5 1 L7 5 L5 7 Q6 10 9 11 L11 9 L13 11 L12 14 Q3 13 2 2Z" fill="var(--teal)"/>
    <rect x="1" y="25" width="12" height="9" fill="var(--teal)"/>
    <polyline points="1,25 7,30 13,25" fill="none" stroke="var(--navy)" stroke-width="1.2"/>
  </svg>
  <div class="abs footer-line" style="left:388px;top:77px">TEL&nbsp; 1800-555-719<br>EMAIL&nbsp; HELLO@QUENMARSHART.COM</div>
  <div class="abs social" style="left:993px;background:#3b5a9a"></div>
  <div class="abs social" style="left:1042px;background:#35b6e4"></div>
  <div class="abs social" style="left:1090px;background:#f08a24"></div>
  <div class="abs copyright">(c) 2016, Quenmarsh. All Right Reserved.</div>
</footer>

</body>
</html>
```